Larkin Ridge Provisions Co Website Creation

We need a website designed that goes along with our western/cattle brand vibe that our logo has. We are going to need a couple different pages including: About Us, Meat Boxes, Recipes, Contact Us.

We are going to need a shop so that people may visit the website and order meat boxes to be shipped or delivered at their home. Our mission is to provide the highest quality meat that every family can afford.

Would love to see the website design with lots of mountain range backgrounds and create a feel of open range beef that has a tradition of providing great beef. Family owned business that has been raising cattle for over 30 years.

Love the colors of using dark greens, browns, Tans, Blacks

```html
<!DOCTYPE html>
<html lang="en">
<head>
<meta charset="utf-8">
<title>Larkin Ridge Provisions Co</title>
<link rel="stylesheet" href="https://fonts.googleapis.com/css2?family=Bebas+Neue&family=Cabin:wght@400;500;600&display=swap">
<style>
:root{
  --green:#1f6f1b;
  --green-dark:#17570f;
  --green-deep:#12460c;
  --ink:#111111;
  --white:#ffffff;
  --field:#f1f1f1;
  --star:#e8862a;
  --head:'Bebas Neue', sans-serif;
  --body:'Cabin', sans-serif;
}
*{box-sizing:border-box;margin:0;padding:0}
html,body{width:1200px;height:3222px;overflow:hidden}
body{position:relative;background:var(--white);font-family:var(--body);color:var(--ink)}
.abs{position:absolute}
.btn{position:absolute;display:flex;align-items:center;justify-content:center;border-radius:20px;background:var(--green);color:var(--white);font-size:15px;font-weight:500}

/* nav */
.nav{position:absolute;left:0;top:0;width:1200px;height:99px;background:var(--white)}
.brand{position:absolute;left:68px;top:37px;display:flex;align-items:center;gap:8px;font-weight:600;font-size:20px;color:var(--green)}
.brand-dot{width:22px;height:22px;border-radius:50%;background:var(--green)}
.nav-link{position:absolute;top:40px;font-size:20px;font-weight:500;color:var(--ink)}
.nav-icon{position:absolute;top:37px;width:31px;height:31px;border-radius:50%;background:var(--green);display:flex;align-items:center;justify-content:center}

/* hero */
.hero{position:absolute;left:0;top:99px;width:1200px;height:540px;
  background:
    radial-gradient(ellipse 420px 260px at 260px 460px,rgba(120,170,40,.85),rgba(120,170,40,0) 70%),
    radial-gradient(ellipse 520px 300px at 980px 120px,rgba(24,44,22,.85),rgba(24,44,22,0) 75%),
    radial-gradient(ellipse 380px 240px at 700px 60px,rgba(150,170,120,.55),rgba(150,170,120,0) 70%),
    radial-gradient(ellipse 460px 260px at 1050px 470px,rgba(38,70,24,.8),rgba(38,70,24,0) 75%),
    radial-gradient(ellipse 300px 160px at 420px 380px,rgba(90,60,30,.35),rgba(90,60,30,0) 70%),
    linear-gradient(180deg,#3a5a2a 0%,#4f7f2c 40%,#6aa02e 70%,#5b8c24 100%)}
.hero::after{content:"";position:absolute;inset:0;background:linear-gradient(90deg,rgba(0,0,0,.28) 0%,rgba(0,0,0,.08) 55%,rgba(0,0,0,0) 100%)}
.hero > *{z-index:1}
.hero-title{position:absolute;left:68px;top:66px;font-family:var(--head);font-weight:400;font-size:74px;line-height:1;color:var(--white);letter-spacing:1px}
.hero-text{position:absolute;left:68px;top:167px;width:560px;font-size:18px;line-height:22.5px;color:var(--white);font-weight:500}
.hero-next{position:absolute;left:1080px;top:217px;width:44px;height:44px;border:2px solid var(--white);border-radius:50%}
.bar{position:absolute;top:489px;height:4px;width:140px;background:rgba(255,255,255,.45)}
.bar.on{background:var(--white)}

/* about */
.about-photo{position:absolute;left:63px;top:709px;width:500px;height:307px;border-radius:4px;
  background:
    radial-gradient(ellipse 90px 140px at 60px 110px,rgba(170,60,75,.95),rgba(170,60,75,0) 75%),
    radial-gradient(ellipse 90px 140px at 150px 100px,rgba(185,75,85,.9),rgba(185,75,85,0) 75%),
    radial-gradient(ellipse 100px 150px at 390px 100px,rgba(180,65,80,.95),rgba(180,65,80,0) 75%),
    radial-gradient(ellipse 80px 120px at 460px 150px,rgba(160,55,70,.9),rgba(160,55,70,0) 75%),
    radial-gradient(ellipse 120px 60px at 400px 270px,rgba(200,110,110,.85),rgba(200,110,110,0) 75%),
    radial-gradient(ellipse 60px 110px at 250px 120px,rgba(210,225,240,.8),rgba(210,225,240,0) 75%),
    linear-gradient(180deg,#2c3644 0%,#4b5a6c 55%,#6f7c8a 75%,#3a4552 100%)}
.sec-title{font-family:var(--head);font-weight:400;font-size:38px;color:var(--green);line-height:1}
.about-copy{position:absolute;left:622px;top:767px;width:490px;font-size:12.4px;line-height:16.2px;color:#333}
.about-copy p+p{margin-top:13px}

/* meat boxes */
.boxes{position:absolute;left:0;top:1086px;width:1200px;height:647px;background:var(--green)}
.boxes .sec-title{position:absolute;left:0;width:1200px;text-align:center;top:54px;color:var(--white)}
.boxes-text{position:absolute;left:163px;top:111px;width:857px;text-align:center;font-size:12.5px;line-height:16px;color:var(--white)}
.arrow-btn{position:absolute;width:44px;height:44px;border-radius:50%;border:2px solid currentColor;display:flex;align-items:center;justify-content:center}
.card{position:absolute;top:219px;width:325px;height:315px;background:var(--white);clip-path:polygon(0 0,100% 0,90% 100%,10% 100%);border-radius:18px}
.tray{position:absolute;left:96px;top:29px;width:135px;height:92px;border-radius:12px;
  background:radial-gradient(ellipse 48px 30px at 50% 50%,#d45a6c 0%,#b23a4f 55%,rgba(120,30,45,0) 100%),linear-gradient(160deg,#3a3a3a,#0e0e0e)}
.card-name{position:absolute;left:57px;top:178px;font-family:var(--head);font-size:29px;color:var(--green)}
.card-kg{position:absolute;right:60px;top:178px;font-family:var(--head);font-size:29px;color:var(--green)}
.stars{position:absolute;left:57px;top:208px;font-size:17px;letter-spacing:6px;color:var(--star)}
.price{position:absolute;left:57px;top:260px;font-family:var(--head);font-size:36px;color:var(--green)}
.cart-btn{position:absolute;left:166px;top:263px;width:98px;height:31px;border:1.5px solid var(--green);border-radius:16px;font-size:12px;color:var(--green);display:flex;align-items:center;justify-content:center}
.dot{position:absolute;top:600px;width:12px;height:12px;border-radius:50%;background:rgba(255,255,255,.8)}

/* recipes */
.recipes-title{position:absolute;left:0;width:1176px;text-align:center;top:1795px}
.recipes-text{position:absolute;left:200px;top:1852px;width:780px;text-align:center;font-size:12.5px;line-height:16px;color:#222}
.tile{position:absolute;border-radius:4px;overflow:hidden}
.tile::after{content:"";position:absolute;left:0;right:0;bottom:0;height:45%;background:linear-gradient(180deg,rgba(0,0,0,0),rgba(0,0,0,.35))}
.tile span{position:absolute;left:32px;bottom:18px;font-size:18px;font-weight:600;color:var(--white);z-index:1}

/* contact */
.contact{position:absolute;left:0;top:2400px;width:1200px;height:475px;
  background:
    radial-gradient(ellipse 380px 120px at 300px 60px,rgba(190,205,220,.55),rgba(190,205,220,0) 70%),
    radial-gradient(ellipse 340px 110px at 900px 40px,rgba(170,185,200,.5),rgba(170,185,200,0) 70%),
    radial-gradient(ellipse 500px 160px at 350px 380px,rgba(110,130,40,.75),rgba(110,130,40,0) 75%),
    radial-gradient(ellipse 420px 140px at 1000px 300px,rgba(30,55,35,.8),rgba(30,55,35,0) 75%),
    linear-gradient(180deg,#3e556c 0%,#4f6778 28%,#3d5748 52%,#44602e 75%,#2e4420 100%)}
.contact::after{content:"";position:absolute;inset:0;background:rgba(10,20,30,.22)}
.contact > *{z-index:1}
.contact .sec-title{position:absolute;left:65px;top:82px;color:var(--white)}
.contact-text{position:absolute;left:65px;top:141px;width:330px;font-size:13px;line-height:16px;color:var(--white)}
.info-icon{position:absolute;left:64px;width:39px;height:39px;border-radius:50%;background:var(--white);display:flex;align-items:center;justify-content:center}
.info-text{position:absolute;left:121px;font-size:13px;line-height:16px;color:var(--white)}
.form{position:absolute;left:590px;top:59px;width:543px;height:363px;background:var(--white);border-radius:30px}
.form h3{position:absolute;left:0;width:543px;top:30px;text-align:center;font-size:22px;font-weight:500;color:var(--green)}
.field{position:absolute;height:29px;border-radius:14px;background:var(--field);font-size:11px;color:#888;padding:8px 15px}

/* footer */
.footer{position:absolute;left:0;top:2875px;width:1200px;height:347px;background:var(--ink);color:var(--white)}
.foot-brand{position:absolute;left:65px;top:95px;display:flex;align-items:center;gap:12px;font-size:26px;font-weight:600;color:var(--white)}
.foot-brand i{width:34px;height:34px;border-radius:50%;background:var(--white);display:block}
.foot-text{position:absolute;left:65px;top:215px;width:330px;font-size:13px;line-height:16px}
.col-head{position:absolute;top:57px;font-size:17px;font-weight:500;color:var(--green)}
.col-item{position:absolute;font-size:13px}
.col-item::before{content:"›";position:absolute;left:-25px;top:-3px;font-size:17px}
.news-input{position:absolute;left:898px;top:140px;width:197px;height:30px;border-radius:15px;background:var(--white);color:#777;font-size:11px;padding:8px 24px}
.news-go{position:absolute;left:1058px;top:140px;width:37px;height:30px;border-radius:15px;background:var(--green);display:flex;align-items:center;justify-content:center}
.social{position:absolute;top:224px;width:32px;height:32px;border-radius:50%;background:var(--white);border:3px solid var(--green)}
.foot-rule{position:absolute;left:0;top:295px;width:1200px;height:1px;background:#444}
.foot-bottom{position:absolute;top:315px;font-size:12px}
</style>
</head>
<body>

<header class="nav">
  <div class="brand"><span class="brand-dot"></span>Larkin Ridge Provisions Co</div>
  <a class="nav-link" style="left:462px">Home</a>
  <a class="nav-link" style="left:555px">About us</a>
  <a class="nav-link" style="left:674px">Meat Boxes</a>
  <a class="nav-link" style="left:814px">Recipes</a>
  <a class="nav-link" style="left:922px">Contact us</a>
  <div class="nav-icon" style="left:1045px"><svg width="16" height="16" viewBox="0 0 16 16" fill="none" stroke="#fff" stroke-width="1.3"><path d="M1 2h2l2 8h8l1.5-6H4"/><circle cx="6" cy="13" r="1"/><circle cx="12" cy="13" r="1"/></svg></div>
  <div class="nav-icon" style="left:1101px"><svg width="16" height="16" viewBox="0 0 16 16" fill="none" stroke="#fff" stroke-width="1.3"><circle cx="8" cy="5" r="3"/><path d="M2.5 14c.5-3 3-4.5 5.5-4.5s5 1.5 5.5 4.5z"/></svg></div>
</header>

<section class="hero" role="img" aria-label="Cattle grazing on a green mountain pasture with pine forest">
  <h1 class="hero-title">Welcome to Larkin Ridge Provisions Co</h1>
  <p class="hero-text">Lorem ipsum dolor sit amet, cons ectetuer adipiscing elit, sed diam nonummy nibh euismod tincidunt ut laoreet dolore magna aliquam erat volutpat. Ut wisi enim ad minim veniam, quis nostrud exerci tation ullamcorper suscipit lobortis nisl ut aliquip</p>
  <div class="btn" style="left:68px;top:291px;width:126px;height:34px">Order Now</div>
  <div class="hero-next"><svg width="40" height="40" viewBox="0 0 40 40" fill="none" stroke="#fff" stroke-width="2"><path d="M17 12l8 8-8 8"/></svg></div>
  <div class="bar on" style="left:669px"></div>
  <div class="bar" style="left:826px"></div>
  <div class="bar" style="left:982px"></div>
</section>

<section>
  <div class="about-photo" role="img" aria-label="Cold storage room with hanging beef carcasses"></div>
  <h2 class="sec-title abs" style="left:622px;top:713px">About Us</h2>
  <div class="about-copy">
    <p>Lorem ipsum dolor sit amet, cons ectetuer adipiscing elit, sed diam nonummy nibh euismod tincidunt ut laoreet dolore magna aliquam erat volutpat. Ut wisi enim ad minim veniam, quis nostrud exerci tation ullamcorper suscipit lobortis nisl ut aliquip ex ea commodo consequat.</p>
    <p>Lorem ipsum dolor sit amet, consectetuer adipiscing elit, sed diam nonummy nibh euismod tincidunt ut laoreet dolore magna aliquam erat volutpat. Ut wisi enim ad minim veniam, quis nostrud exerci tation ullamcorper suscipit lobortis nisl ut aliquip ex ea commodo consequat. Duis autem vel eum iriure dolor in hendrerit in vulputate velit esse molestie consequat, vel illum dolore eu feugiat nulla facilisis at vero eros et accumsan et iusto odio dignissim qui blandit praesent luptatum zzril delenit augue duis dolore te feugait nulla facilisi.</p>
  </div>
  <div class="btn" style="left:622px;top:982px;width:126px;height:34px">Read More</div>
</section>

<section class="boxes">
  <h2 class="sec-title">Meat Boxes</h2>
  <div class="arrow-btn" style="left:1033px;top:40px;color:#fff"><svg width="16" height="16" viewBox="0 0 16 16" fill="none" stroke="#fff" stroke-width="1.6"><path d="M10 2L4 8l6 6"/></svg></div>
  <div class="arrow-btn" style="left:1089px;top:40px;color:#fff"><svg width="16" height="16" viewBox="0 0 16 16" fill="none" stroke="#fff" stroke-width="1.6"><path d="M6 2l6 6-6 6"/></svg></div>
  <p class="boxes-text">Lorem ipsum dolor sit amet, cons ectetuer adipiscing elit, sed diam nonummy nibh euismod tincidunt ut laoreet dolore magna aliquam erat volutpat. Ut wisi enim ad minim veniam, quis nostrud exerci tation ullamcorper suscipit lobortis nisl ut aliquip ex ea commodo consequat.</p>

  <article class="card" style="left:63px">
    <div class="tray" role="img" aria-label="Packaged beef steak in a black tray"></div>
    <div class="card-name">Beef Meat</div><div class="card-kg">1KG</div>
    <div class="stars">★★★★</div>
    <div class="price">16$</div><div class="cart-btn">Add to Cart</div>
  </article>
  <article class="card" style="left:438px">
    <div class="tray" role="img" aria-label="Packaged beef steak in a black tray"></div>
    <div class="card-name">Beef Meat</div><div class="card-kg">2KG</div>
    <div class="stars">★★★★</div>
    <div class="price">26$</div><div class="cart-btn">Add to Cart</div>
  </article>
  <article class="card" style="left:814px">
    <div class="tray" role="img" aria-label="Packaged beef steak in a black tray"></div>
    <div class="card-name">Beef Meat</div><div class="card-kg">3KG</div>
    <div class="stars">★★★★</div>
    <div class="price">46$</div><div class="cart-btn">Add to Cart</div>
  </article>

  <span class="dot" style="left:561px;background:#fff"></span>
  <span class="dot" style="left:587px"></span>
  <span class="dot" style="left:613px"></span>
</section>

<section>
  <h2 class="sec-title recipes-title">Recipes</h2>
  <div class="arrow-btn" style="left:1033px;top:1790px;color:var(--green)"><svg width="16" height="16" viewBox="0 0 16 16" fill="none" stroke="#1f6f1b" stroke-width="1.6"><path d="M10 2L4 8l6 6"/></svg></div>
  <div class="arrow-btn" style="left:1089px;top:1790px;color:var(--green)"><svg width="16" height="16" viewBox="0 0 16 16" fill="none" stroke="#1f6f1b" stroke-width="1.6"><path d="M6 2l6 6-6 6"/></svg></div>
  <p class="recipes-text">Lorem ipsum dolor sit amet, cons ectetuer adipiscing elit, sed diam nonummy nibh euismod tincidunt ut laoreet dolore magna aliquam erat volutpat. Ut wisi enim ad minim veniam, quis nostrud exerci tation ullamcorper suscipit lobortis nisl ut aliquip ex ea commodo consequat.</p>

  <div class="tile" style="left:63px;top:1925px;width:431px;height:205px;background:radial-gradient(ellipse 130px 60px at 170px 85px,rgba(160,110,50,.9),rgba(160,110,50,0) 75%),radial-gradient(ellipse 110px 55px at 280px 140px,rgba(160,50,60,.9),rgba(160,50,60,0) 75%),linear-gradient(160deg,#1f1c18 0%,#3a2a1e 50%,#2a1e16 100%)" role="img" aria-label="Sliced beef wellington on a wooden board"><span>Beef Wellington</span></div>
  <div class="tile" style="left:507px;top:1925px;width:284px;height:205px;background:radial-gradient(ellipse 70px 55px at 150px 75px,rgba(190,120,50,.95),rgba(190,120,50,0) 80%),radial-gradient(ellipse 140px 40px at 120px 165px,rgba(170,120,70,.9),rgba(170,120,70,0) 80%),linear-gradient(160deg,#1c1815 0%,#2c2520 60%,#3a2e24 100%)" role="img" aria-label="Hamburger on a wooden board"><span>Hamburger</span></div>
  <div class="tile" style="left:803px;top:1929px;width:333px;height:403px;background:radial-gradient(ellipse 130px 120px at 190px 120px,rgba(200,70,40,.9),rgba(200,70,40,0) 80%),radial-gradient(ellipse 150px 110px at 200px 290px,rgba(215,130,95,.85),rgba(215,130,95,0) 80%),linear-gradient(170deg,#a88a70 0%,#d9c8b6 40%,#eee8e0 100%)" role="img" aria-label="Sliced meatloaf with glaze on a white plate"><span>Meatloaf</span></div>
  <div class="tile" style="left:63px;top:2144px;width:276px;height:188px;background:radial-gradient(ellipse 75px 65px at 95px 80px,rgba(80,45,28,.95),rgba(40,30,25,.9) 70%,rgba(40,30,25,0) 100%),linear-gradient(135deg,#8e8c88 0%,#a6a4a0 50%,#7e7c78 100%)" role="img" aria-label="Pan of beef stew with vegetables"><span>Beef Stew</span></div>
  <div class="tile" style="left:352px;top:2144px;width:439px;height:188px;background:radial-gradient(ellipse 170px 70px at 210px 110px,rgba(120,55,35,.95),rgba(120,55,35,0) 80%),radial-gradient(ellipse 220px 80px at 220px 130px,rgba(225,200,160,.9),rgba(225,200,160,0) 85%),linear-gradient(135deg,#4a1a16 0%,#a8302a 45%,#6e2220 100%)" role="img" aria-label="Shredded beef fajitas on a tortilla"><span>Beef Fajitas</span></div>
</section>

<section class="contact" role="img" aria-label="Cattle on an alpine meadow below snowy mountains">
  <h2 class="sec-title">Contact Us</h2>
  <p class="contact-text">Lorem ipsum dolor sit amet, cons ectetuer adipiscing elit, sed diam nonummy nibh euismod tincidunt ut</p>
  <div class="info-icon" style="top:203px"><svg width="18" height="18" viewBox="0 0 24 24" fill="#1f6f1b"><path d="M6.6 10.8a15 15 0 006.6 6.6l2.2-2.2c.3-.3.7-.4 1-.2 1.1.4 2.3.6 3.6.6.6 0 1 .4 1 1V20c0 .6-.4 1-1 1A17 17 0 013 4c0-.6.4-1 1-1h3.5c.6 0 1 .4 1 1 0 1.3.2 2.5.6 3.6.1.3 0 .7-.2 1z"/></svg></div>
  <div class="info-text" style="top:215px">0198 765 432</div>
  <div class="info-icon" style="top:269px"><svg width="18" height="18" viewBox="0 0 24 24" fill="none" stroke="#1f6f1b" stroke-width="2.2"><path d="M12 22s7-7 7-12a7 7 0 00-14 0c0 5 7 12 7 12z"/><circle cx="12" cy="10" r="2.5"/></svg></div>
  <div class="info-text" style="top:274px">123,Lorem ipsum dolor sit ame,<br>nonummy nibh euismod, 1234.</div>
  <div class="info-icon" style="top:337px"><svg width="20" height="20" viewBox="0 0 24 24" fill="none" stroke="#1f6f1b" stroke-width="1.6"><circle cx="12" cy="12" r="9"/><path d="M3 12h18M12 3c3 3 3 15 0 18M12 3c-3 3-3 15 0 18"/></svg></div>
  <div class="info-text" style="top:349px">www.larkinridgeprovisions.com</div>

  <form class="form">
    <h3>Any questions ?&nbsp; Just write us a message!</h3>
    <div class="field" style="left:60px;top:89px;width:206px">Your First Name</div>
    <div class="field" style="left:278px;top:89px;width:206px">Your last name</div>
    <div class="field" style="left:60px;top:132px;width:206px">Phone .No</div>
    <div class="field" style="left:278px;top:132px;width:206px">e-Mail</div>
    <div class="field" style="left:60px;top:176px;width:424px;height:87px;border-radius:12px;font-size:13px;padding:14px 18px">Message...</div>
    <div class="btn" style="left:60px;top:285px;width:424px;height:41px;font-size:15px">Submit</div>
  </form>
</section>

<footer class="footer">
  <div class="foot-brand"><i></i>Larkin Ridge Provisions Co</div>
  <p class="foot-text">Lorem ipsum dolor sit amet, cons ectetuer adipiscing elit, sed diam nonummy nibh euismod tincidunt ut</p>

  <div class="col-head" style="left:479px">Quick Link</div>
  <div class="col-item" style="left:512px;top:101px">Home</div>
  <div class="col-item" style="left:512px;top:135px">About us</div>
  <div class="col-item" style="left:512px;top:169px">Meat Box</div>
  <div class="col-item" style="left:512px;top:203px">Recipes</div>
  <div class="col-item" style="left:512px;top:236px">Contact us</div>

  <div class="col-head" style="left:694px">Recipes</div>
  <div class="col-item" style="left:727px;top:101px">Hamburger</div>
  <div class="col-item" style="left:727px;top:135px">Beef Stew</div>
  <div class="col-item" style="left:727px;top:169px">Meatloaf</div>
  <div class="col-item" style="left:727px;top:203px">Beef Wellington</div>
  <div class="col-item" style="left:727px;top:236px">Pot Roast</div>

  <div class="col-head" style="left:898px">News Letter</div>
  <p class="abs" style="left:898px;top:100px;width:250px;font-size:13px;line-height:16px">Lorem ipsum dolor sit amet, cons ectetuer nonummy nibh euismod tincidunt ut</p>
  <div class="news-input">Enter your mail</div>
  <div class="news-go"><svg width="20" height="10" viewBox="0 0 20 10" fill="none" stroke="#fff" stroke-width="1.4"><path d="M1 5h17M14 1l4 4-4 4"/></svg></div>
  <div class="col-head" style="left:898px;top:186px">Connect with us</div>
  <span class="social" style="left:898px"></span>
  <span class="social" style="left:940px"></span>
  <span class="social" style="left:981px"></span>
  <span class="social" style="left:1024px"></span>

  <div class="foot-rule"></div>
  <div class="foot-bottom" style="left:67px">© 2024&nbsp; All Rights Reserved | Larkin Ridge Provisions Co</div>
  <div class="foot-bottom" style="left:1058px">Privacy policy</div>
</footer>

</body>
</html>
```